Food Safety 1-California workers only

3.25" by 4.5" Black and White Magazine Ad
This ad is to train California workers only.
Workers will be trained on: Food Safety, FSMA (Food Safety Modernization Act), using equipment safety, food processing production skills, worker safety, supervisory skills, communication skills.
"FREE TRAINING", The company does the training or Keystone Learning will provide the training.
Training grants range from $100,000 to $400,000.
Companies must be in business for profit.
Companies must train 200 employees or more.
This program is for California workers only.
Incumbent or new-hires are eligible.

Target Market(s)

California food processors, farms, food packaging, food processors, companies under FSMA, food safety, food production who need to train employees.

Industry/Entity Type

Food Production

Font styles to use
Serif
Sans Serif

Colors

Designer to choose colors to be used in the design.

Requirements
Must have
• This is a 3.25 inch by 4.5 inch magazine ad. It must be black and white. No color.
• The deliverable must be in basic PhotoShop. The ad does not need to include any graphics and be text only if needed. If you have a black and white graphic that will show well.
• Look at www.KLGFoodSafety..com
• Use the text from "MEALBOX-Photoshop-052018" file as your starting point.
Nice to have
• A black and white graphic about food. See www.KLGFoodSafety.com
Should not have
• No color.

```html
<!DOCTYPE html>
<html lang="en">
<head>
<meta charset="utf-8">
<title>Free Training – Keystone Learning</title>
<link rel="stylesheet" href="https://fonts.googleapis.com/css2?family=Open+Sans:wght@700;800&family=Arimo:wght@700&display=swap">
<style>
  :root {
    --ink: #000000;
    --paper: #ffffff;
    --produce-light: #e6e6e6;
    --produce-dark: #8a8a8a;
  }
  * { margin: 0; padding: 0; box-sizing: border-box; }
  html, body {
    width: 867px;
    height: 1200px;
    overflow: hidden;
    background: var(--ink);
  }
  .ad {
    position: relative;
    width: 867px;
    height: 1200px;
    background: var(--ink);
    color: var(--paper);
    font-family: "Arimo", Arial, sans-serif;
  }
  .headline {
    position: absolute;
    left: 0;
    top: 10px;
    width: 867px;
    height: 130px;
  }
  .headline text {
    font-family: "Open Sans", "Myriad Pro", sans-serif;
    font-weight: 800;
    font-size: 134px;
    fill: var(--paper);
  }
  .topics {
    position: absolute;
    top: 155px;
    width: 100%;
    text-align: center;
    font-size: 19.5px;
    font-weight: 700;
    letter-spacing: 0.2px;
  }
  .slogan {
    position: absolute;
    left: 0;
    top: 240px;
    width: 867px;
    height: 130px;
  }
  .slogan text {
    font-family: "Open Sans", "Myriad Pro", sans-serif;
    font-weight: 700;
    font-size: 61px;
    fill: var(--paper);
  }
  .qualify {
    position: absolute;
    left: 19px;
    top: 494px;
    font-size: 24px;
    line-height: 29.4px;
    font-weight: 700;
  }
  .qualify ul { list-style: none; }
  .qualify li {
    position: relative;
    padding-left: 32px;
  }
  .qualify li::before {
    content: "";
    position: absolute;
    left: 1px;
    top: 12px;
    width: 6px;
    height: 6px;
    background: var(--paper);
  }
  .contact {
    position: absolute;
    left: 19px;
    top: 888px;
    font-size: 24px;
    line-height: 29.4px;
    font-weight: 700;
    font-style: normal;
  }
  .produce-art {
    position: absolute;
    left: 467px;
    top: 805px;
    width: 382px;
    height: 302px;
    border-radius: 48% 52% 40% 45% / 55% 50% 45% 42%;
    background: radial-gradient(ellipse at 45% 40%, var(--produce-light), var(--produce-dark));
  }
</style>
</head>
<body>
  <main class="ad">
    <svg class="headline" viewBox="0 0 867 130" aria-label="Free Training">
      <text x="18" y="118" textLength="831" lengthAdjust="spacingAndGlyphs">FREE TRAINING</text>
    </svg>

    <p class="topics">FOOD SAFETY (FSMA) PRODUCTION SKILLS &amp; WORKER SAFETY</p>

    <svg class="slogan" viewBox="0 0 867 130" aria-label="We do the training and the state pays for it!">
      <text x="28" y="57" textLength="814" lengthAdjust="spacingAndGlyphs">“WE DO THE TRAINING AND</text>
      <text x="78" y="115" textLength="712" lengthAdjust="spacingAndGlyphs">THE STATE PAYS FOR IT!”</text>
    </svg>

    <section class="qualify">
      <p>How to qualify:</p>
      <ul>
        <li>Train California Workers Only</li>
        <li>Trainees must earn $11/hour</li>
        <li>Full-time workers only</li>
        <li>Employees must attend at least 8 Hours of training</li>
        <li>You must train 200 or more employees</li>
        <li>Incumbent or New-Hire workers are eligible</li>
        <li>Seasonal workers are eligible</li>
      </ul>
    </section>

    <address class="contact">
      Contact:<br>
      Marcus Hale<br>
      Keystone Learning Company, Inc.<br>
      1800 Meadowlark Parkway<br>
      Suite 250<br>
      Irvine, CA 92604<br>
      www.KLGCAL.com<br>
      www.KLGFoodSafety.com<br>
      email: Marcus.Hale@KLGCAL.com<br>
      Phone: (949) 555-0142
    </address>

    <div class="produce-art" role="img" aria-label="Line illustration of fresh vegetables: corn cobs, a tomato, a potato and a carrot"></div>
  </main>
</body>
</html>
```